Banner Ad Design - A moving box for Tobias!

This ad will promote the purchase of a moving box for the Wendle's.

You can try and incorporate the attached graphic that will be on the moving box, although it may be too small. You may need to design you on creative, attention getting graphic.

A few sayings we have below are:

"Give Tobias the Boot"
"Box Up Tobias"
"Out with the Wendle's"
"Boot out Tobias"
"Toby & Sam Gotta Go"

You can a small symbol of a moving box sent directly to the "Cobalt Hall".
Updates

Requested Specs for ad design:

300 x 250  40K Max (Gif or JPG)  Max :15 Animation

Target Market(s)

conservation websites and blogs.

Industry/Entity Type

House

Requirements
Must have
• coded to link back to our website.

bold and attention grabbing.

```html
<!DOCTYPE html>
<html lang="en">
<head>
<meta charset="utf-8">
<title>Out with the Wendle's – Banner</title>
<link rel="stylesheet" href="https://fonts.googleapis.com/css2?family=Lilita+One&family=Roboto:ital,wght@1,900&display=swap">
<style>
  :root {
    --red: #e8141b;
    --ink: #1a1a1a;
    --blue: #1d3f9a;
    --paper: #ffffff;
    --frame: #c9d3e2;
    --engraving-light: #e9e9e9;
    --engraving-dark: #9a9a9a;
    --cardboard-light: #e2b777;
    --cardboard-dark: #b5803c;
  }
  html, body {
    margin: 0;
    padding: 0;
    overflow: hidden;
    background: var(--paper);
  }
  .banner {
    position: relative;
    width: 1200px;
    height: 148px;
    box-sizing: border-box;
    border: 2px solid var(--frame);
    background: var(--paper);
    overflow: hidden;
  }
  .hall-illustration {
    position: absolute;
    left: 0;
    top: 0;
    width: 290px;
    height: 144px;
    background: linear-gradient(180deg, var(--engraving-light) 0%, var(--engraving-dark) 100%);
  }
  .headline {
    position: absolute;
    left: 300px;
    width: 590px;
    top: 4px;
    margin: 0;
    text-align: center;
    font-family: "Lilita One", "Arial Black", sans-serif;
    font-weight: 400;
    font-size: 58px;
    line-height: 1;
    color: var(--red);
    text-shadow: 2px 2px 0 var(--ink), -1px -1px 0 var(--ink), 1px -1px 0 var(--ink), -1px 1px 0 var(--ink);
    letter-spacing: 0.5px;
  }
  .tagline {
    position: absolute;
    left: 300px;
    width: 590px;
    top: 70px;
    margin: 0;
    text-align: center;
    font-family: "Roboto", Arial, sans-serif;
    font-style: italic;
    font-weight: 900;
    font-size: 22px;
    line-height: 29px;
    color: var(--red);
  }
  .box-illustration {
    position: absolute;
    left: 898px;
    top: 8px;
    width: 158px;
    height: 136px;
    background: linear-gradient(135deg, var(--cardboard-light) 0%, var(--cardboard-dark) 100%);
  }
  .party-mark {
    position: absolute;
    left: 1066px;
    top: 18px;
    width: 104px;
    height: 110px;
    display: flex;
    flex-direction: column;
    align-items: center;
    justify-content: center;
    gap: 8px;
  }
  .party-mark .dot {
    width: 26px;
    height: 26px;
    background: var(--blue);
  }
  .party-mark .name {
    font-family: "Roboto", Arial, sans-serif;
    font-style: italic;
    font-weight: 900;
    font-size: 22px;
    line-height: 1;
    color: var(--blue);
    text-align: center;
  }
  .cta {
    position: absolute;
    right: 2px;
    top: 0;
    height: 144px;
    width: 26px;
    display: flex;
    align-items: center;
    justify-content: center;
    color: var(--blue);
    text-decoration: none;
    font-family: "Roboto", Arial, sans-serif;
    font-weight: 900;
    font-size: 16px;
    writing-mode: vertical-rl;
    letter-spacing: 1px;
  }
</style>
</head>
<body>
  <a class="banner" href="#" style="display:block;text-decoration:none;">
    <div class="hall-illustration" role="img" aria-label="Engraved illustration of Cobalt Hall"></div>
    <h1 class="headline">Out with the Wendle's</h1>
    <p class="tagline">Send a moving box to the Cobalt Hall as a gift<br>to help them pack up and leave!</p>
    <div class="box-illustration" role="img" aria-label="Cardboard moving box addressed to the Wendle's"></div>
    <div class="party-mark">
      <span class="dot"></span>
      <span class="name">Civic<br>Party</span>
    </div>
    <span class="cta">CLICK NOW</span>
  </a>
</body>
</html>
```